Service Plan Sales Flyer

The Watchpost Depot (www.kelvamart.com) is a commercial security integrator that installs security cameras, access control, intrusion, two-way radios and perimeter security. We require a one page flyer for our service plan for new and existing customers. The price of the service plan is $299/yr and includes the following;
1. Discounted service rate of $118/hr
2. Free remote support ($85/hr without a plan)
3. Free remote training
4. Priority support

Please review our brochure attached and create a one page sales flyer with the end goal of having the client sign up for our annual service plan . The plan will automatically renew every year. Email sales@kelvamart.com.

Target Market(s)

commercial industrial clients - no residential

Industry/Entity Type

review our website at www.kelvamart.com

Colors
0054AA
0677BA
7BADD7
CADEEF
E8F1F8
EE7325
F08F49
F5BC92
FAE3D3
FDF4ED

Requirements
Must have
• call to action
Should not have
• too many colors

```html
<!DOCTYPE html>
<html lang="en">
<head>
<meta charset="utf-8">
<title>The Watchpost Depot – Service Plan</title>
<link href="https://fonts.googleapis.com/css2?family=Poppins:wght@500;600;700;800&display=swap" rel="stylesheet">
<style>
:root{
  --navy:#0f2a55;
  --navy-deep:#0a2048;
  --red:#ee4136;
  --white:#ffffff;
  --stage:#1f1f1f;
  --photo-a:#0c1e3a;
  --photo-b:#3f6d98;
}
*{margin:0;padding:0;box-sizing:border-box}
html,body{width:1200px;height:1200px;overflow:hidden;background:var(--stage);font-family:'Poppins',sans-serif}
.flyer{position:absolute;left:163px;top:0;width:873px;height:1200px;background:var(--white);overflow:hidden}
.masthead{position:absolute;left:0;top:0;width:100%;height:158px;display:flex;align-items:center;justify-content:center;gap:16px}
.brand-mark{width:44px;height:44px;background:var(--red)}
.brand-block{display:flex;flex-direction:column}
.brand-name{font-size:44px;font-weight:800;color:var(--navy);line-height:1;letter-spacing:-0.5px}
.brand-tagline{font-size:14px;font-weight:600;color:var(--navy);margin-top:8px;text-align:right}
.hero{position:absolute;left:0;top:158px;width:100%;height:354px;background:linear-gradient(160deg,var(--photo-b) 0%,var(--photo-a) 55%,#07142a 100%)}
.hero-copy{position:absolute;left:0;top:205px;width:100%;text-align:center}
.hero-title{font-size:46px;font-weight:800;letter-spacing:-0.5px;line-height:1;-webkit-text-stroke:2px var(--white);paint-order:stroke fill}
.hero-title .t-navy{color:var(--navy)}
.hero-title .t-red{color:var(--red)}
.hero-sub{margin-top:12px;font-size:19.5px;font-weight:700;color:var(--white);line-height:24px;text-shadow:0 1px 3px rgba(0,0,0,.6)}
.price-band{position:absolute;left:0;top:512px;width:100%;height:69px;background:var(--white)}
.price-label{position:absolute;left:73px;top:0;height:69px;line-height:69px;font-size:26.5px;font-weight:700;color:var(--navy);letter-spacing:-0.3px}
.price-tag{position:absolute;left:563px;top:0;width:310px;height:69px;background:var(--red);clip-path:polygon(10px 0,100% 0,100% 100%,0 100%);color:var(--white);font-size:44px;font-weight:700;line-height:69px;padding-left:58px}
.plan{position:absolute;left:0;top:581px;width:100%;height:488px;background:linear-gradient(180deg,var(--navy) 0%,var(--navy-deep) 100%)}
.plan-intro{position:absolute;left:121px;top:22px;font-size:27px;font-weight:600;color:var(--red)}
.benefits{position:absolute;left:73px;top:72px;list-style:none}
.benefit{display:flex;align-items:center;height:31px;margin-bottom:14.5px;font-size:26px;font-weight:700;color:var(--white);letter-spacing:-0.2px}
.benefit svg{width:32px;height:32px;margin-right:17px;flex:none}
.renew-note{position:absolute;left:73px;top:268px;width:729px;height:31px;border-radius:6px;background:var(--white);text-align:center;font-size:20.5px;font-weight:700;color:#2a2f7a;line-height:31px;letter-spacing:1px}
.values{position:absolute;left:60px;top:350px;width:300px;text-align:center;font-size:31px;font-weight:500;color:var(--white);line-height:31px;letter-spacing:1px}
.services{position:absolute;left:377px;top:328px;display:flex;gap:22px}
.service{width:90px;text-align:center}
.service svg{width:90px;height:90px;display:block}
.service-label{margin-top:4px;font-size:5.5px;font-weight:600;color:var(--white);white-space:nowrap;margin-left:-10px;margin-right:-10px}
.cta{position:absolute;left:75px;top:1040px;width:718px;height:75px;background:var(--red);clip-path:polygon(16px 0,100% 0,98% 100%,0 100%);display:flex;align-items:center;padding-left:30px}
.cta-label{font-size:35px;font-weight:800;color:var(--navy);letter-spacing:-0.5px}
.cta-phone-icon{width:40px;height:40px;margin:0 14px 0 24px}
.cta-number{font-size:46px;font-weight:700;color:var(--white);letter-spacing:-0.5px}
.contact{position:absolute;left:73px;top:1130px;width:740px;height:44px;display:flex;align-items:center;color:var(--red)}
.contact svg{width:24px;height:16px;margin-right:10px}
.contact-email{font-size:25px;font-weight:600;letter-spacing:1px}
.contact-sep{font-size:26px;font-weight:600;margin:0 22px 0 36px}
.contact-web{font-size:27px;font-weight:700;letter-spacing:0.5px}
</style>
</head>
<body>
<main class="flyer">
  <header class="masthead">
    <span class="brand-mark"></span>
    <div class="brand-block">
      <span class="brand-name">THE WATCHPOST DEPOT</span>
      <span class="brand-tagline">Commercial &amp; Industrial Solutions</span>
    </div>
  </header>

  <section class="hero" role="img" aria-label="Photo of a security operator watching a wall of surveillance monitors in a dark control room">
    <div class="hero-copy">
      <h1 class="hero-title"><span class="t-navy">COMMERCIAL</span> <span class="t-red">SECURITY</span></h1>
      <p class="hero-sub">INTEGRATOR THAT INSTALLS SECURITY CAMERAS,<br>ACCESS CONTROL, INTRUSION, TWO-WAY RADIOS AND<br>PERIMETER SECURITY</p>
    </div>
  </section>

  <section class="price-band">
    <p class="price-label">THE PRICE OF THE SERVICE PLAN IS</p>
    <p class="price-tag">$299/YR</p>
  </section>

  <section class="plan">
    <p class="plan-intro">includes the following :</p>
    <ul class="benefits">
      <li class="benefit"><svg viewBox="0 0 32 32"><circle cx="16" cy="16" r="16" fill="#fff"/><path d="M8 16.5l5.5 5.5L24.5 9" fill="none" stroke="#0f2a55" stroke-width="4" stroke-linecap="round" stroke-linejoin="round"/></svg>DISCOUNTED SERVICE RATE OF $118/HR</li>
      <li class="benefit"><svg viewBox="0 0 32 32"><circle cx="16" cy="16" r="16" fill="#fff"/><path d="M8 16.5l5.5 5.5L24.5 9" fill="none" stroke="#0f2a55" stroke-width="4" stroke-linecap="round" stroke-linejoin="round"/></svg>FREE REMOTE SUPPORT ($85/HR WITHOUT A PLAN)</li>
      <li class="benefit"><svg viewBox="0 0 32 32"><circle cx="16" cy="16" r="16" fill="#fff"/><path d="M8 16.5l5.5 5.5L24.5 9" fill="none" stroke="#0f2a55" stroke-width="4" stroke-linecap="round" stroke-linejoin="round"/></svg>FREE REMOTE TRAINING</li>
      <li class="benefit"><svg viewBox="0 0 32 32"><circle cx="16" cy="16" r="16" fill="#fff"/><path d="M8 16.5l5.5 5.5L24.5 9" fill="none" stroke="#0f2a55" stroke-width="4" stroke-linecap="round" stroke-linejoin="round"/></svg>PRIORITY SUPPORT</li>
    </ul>
    <p class="renew-note">The plan will automatically renew every year</p>

    <p class="values">KNOWLEDGEABLE<br>RELIABLE | EASY</p>

    <div class="services">
      <div class="service">
        <svg viewBox="0 0 90 90"><circle cx="45" cy="45" r="43" fill="#1b3565" stroke="#fff" stroke-width="3"/><circle cx="56" cy="32" r="9" fill="none" stroke="#fff" stroke-width="4"/><path d="M50 39L26 63M33 56l5 5M29 60l4 4" stroke="#fff" stroke-width="4" stroke-linecap="round"/><path d="M20 20l50 50" stroke="#fff" stroke-width="3"/></svg>
        <p class="service-label">ACCESS CONTROL &amp; INTERCOM</p>
      </div>
      <div class="service">
        <svg viewBox="0 0 90 90"><circle cx="45" cy="45" r="43" fill="#1b3565" stroke="#fff" stroke-width="3"/><rect x="28" y="20" width="34" height="50" rx="5" fill="none" stroke="#fff" stroke-width="4"/><rect x="34" y="26" width="22" height="9" fill="#fff"/><g fill="#fff"><rect x="34" y="41" width="5" height="5"/><rect x="42.5" y="41" width="5" height="5"/><rect x="51" y="41" width="5" height="5"/><rect x="34" y="51" width="5" height="5"/><rect x="42.5" y="51" width="5" height="5"/><rect x="51" y="51" width="5" height="5"/></g></svg>
        <p class="service-label">INTRUSION ALARM</p>
      </div>
      <div class="service">
        <svg viewBox="0 0 90 90"><circle cx="45" cy="45" r="43" fill="#1b3565" stroke="#fff" stroke-width="3"/><g stroke="#fff" stroke-width="3" fill="none"><path d="M20 30v35M30 30v35M40 30v35M50 40v25M60 40v25M70 40v25M20 40h50M20 52h50M20 63h50"/><path d="M56 20l12 5v9c0 6-5 10-12 12-7-2-12-6-12-12v-9z" fill="#1b3565"/></g></svg>
        <p class="service-label">PERIMETER SECURITY</p>
      </div>
      <div class="service">
        <svg viewBox="0 0 90 90"><circle cx="45" cy="45" r="43" fill="#1b3565" stroke="#fff" stroke-width="3"/><path d="M48 18v14" stroke="#fff" stroke-width="4"/><path d="M36 40l28-12 6 14-28 12z" fill="#fff"/><path d="M38 50l-8 4v8l-6 2" stroke="#fff" stroke-width="4" fill="none"/></svg>
        <p class="service-label">SURVEILLANCE CAMERAS</p>
      </div>
    </div>
  </section>

  <section class="cta">
    <span class="cta-label">FREE QUOTE</span>
    <svg class="cta-phone-icon" viewBox="0 0 40 40"><path d="M9 5l6 0 3 9-4 3c2 5 6 9 11 11l3-4 9 3v6c0 2-2 3-4 3C18 40 0 22 5 9c0-2 2-4 4-4z" fill="#fff"/><path d="M24 6a12 12 0 0 1 10 10M23 12a6 6 0 0 1 5 5" stroke="#fff" stroke-width="3" fill="none" stroke-linecap="round"/></svg>
    <span class="cta-number">1-877-555-0142</span>
  </section>

  <footer class="contact">
    <svg viewBox="0 0 24 16"><rect x="1" y="1" width="22" height="14" fill="none" stroke="#ee4136" stroke-width="1.5"/><path d="M1 1l11 8 11-8M1 15l8-7M23 15l-8-7" fill="none" stroke="#ee4136" stroke-width="1.5"/></svg>
    <span class="contact-email">sales@kelvamart.com.</span>
    <span class="contact-sep">|</span>
    <span class="contact-web">WWW.KELVAMART.COM</span>
  </footer>
</main>
</body>
</html>
```